Dog Snacks brand needs a new packaging design

Dear Designers,

We are looking for a packaging expert to design our new line of Dog Snacks which contain a relaxing hemp extract (CBD).

Our company is already selling various relaxing cat & dog products , and we would like this new design to reflect the same "style & feeling" as our current products (see attached instructions).

Technical aspects:
- The packaging is a Stand Up Pouch (12x18.5x7cm - see attached instructions).
- Please follow technical guidelines from printer (see attached instructions).
- The packaging will contain 120g of high-quality, semi-moist dog snacks.
- We will be designing 3 differents variations for 3 different flavours: Chicken, Beef & Liver.
- The packaging will be printed with a matt finish.

Design aspects:
- The design should be compatible with our brand identity (i.e. fluffly, pure, relaxing, positive, clean & natural).
- Soft/rounded shapes are preferred.
- Please use our brand's colors (#3BA384, White & Black).
- Please use our company logo (see attached instructions).
- The design also needs to convey a strong sense of professionalism as we are an animal "healthcare" brand.
- If you want to include a dog picture, we would prefer you to use a picture of our official brand ambassador (see attached instructions).
- We have attached a number of packaging examples which we like a lot. (see attached instructions). Please only use those as general inspiration.
- Only original work (no plagiarism will be accepted).

Please don't hesitate to send us a message if you have any questions about the brand, the product or the design requirements.

We look forward to seeing your designs & working on this together !

Thanks & regards,
Marcus

Target Market(s)

Dog owners

Industry/Entity Type

Pet Care

Font styles to use
Sans Serif

Requirements
Must have
• Please see project description.
Nice to have
Should not have

```html
<!DOCTYPE html>
<html lang="en">
<head>
<meta charset="utf-8">
<title>SnuggleBites CBD Treats – Pouch Label</title>
<link href="https://fonts.googleapis.com/css2?family=Raleway:wght@500;600;700&family=Yellowtail&family=Yeseva+One&display=swap" rel="stylesheet">
<style>
  :root {
    --stage: #eef1ef;
    --ink: #1d1d1b;
    --brand-green: #3ba384;
    --white: #ffffff;
    --dog-fur: #ece8e6;
    --dog-shade: #d3cbc9;
    --treat: #b98d62;
  }
  html, body {
    margin: 0;
    width: 1200px;
    height: 824px;
    overflow: hidden;
  }
  body {
    background: var(--stage);
    position: relative;
  }
  .label {
    position: absolute;
    left: 325px;
    top: 32px;
    width: 550px;
    height: 760px;
    display: block;
  }
  .sans { font-family: "Raleway", sans-serif; }
  .brand-name { font-weight: 600; font-size: 27px; letter-spacing: 1px; fill: var(--brand-green); }
  .brand-tag { font-weight: 600; font-size: 12px; fill: var(--brand-green); }
  .band-text { font-weight: 600; font-size: 12px; fill: var(--white); letter-spacing: .5px; }
  .benefits { font-weight: 600; font-size: 15px; fill: var(--white); letter-spacing: 2px; }
  .product-name { font-weight: 600; font-size: 61px; fill: var(--brand-green); letter-spacing: -2px; }
  .cbd-tag { font-weight: 500; font-size: 18px; fill: var(--white); }
  .treats-word { font-family: "Yellowtail", "Pacifico", "Brush Script MT", cursive; font-size: 80px; fill: var(--white); }
  .flavour { font-family: "Yeseva One", serif; }
  .flavour-top { font-size: 33px; fill: var(--white); }
  .flavour-main { font-size: 40px; fill: var(--brand-green); }
  .badge-big { font-weight: 600; fill: var(--brand-green); }
  .badge-small { font-weight: 600; font-size: 10px; fill: var(--brand-green); }
  .claim { font-weight: 600; font-size: 15px; fill: var(--white); }
</style>
</head>
<body>
<svg class="label" viewBox="0 0 550 760" xmlns="http://www.w3.org/2000/svg">
  <rect class="panel" x="0" y="0" width="550" height="760" fill="var(--ink)"/>

  <text class="sans brand-name" x="275" y="76" text-anchor="middle">VERDANEL</text>
  <text class="sans brand-tag" x="310" y="93" text-anchor="middle">For Animals</text>

  <path class="top-band" fill="var(--brand-green)"
        d="M0 100 H210 C245 100 265 120 275 154 C285 120 305 100 340 100 H550 V122 H345 C310 122 290 135 275 154 C260 135 240 122 205 122 H0 Z"/>
  <text class="sans band-text" x="28" y="116">NET WEIGHT 120G</text>
  <text class="sans band-text" x="522" y="116" text-anchor="end">CBD <tspan font-weight="700" font-size="14">250</tspan>mg</text>

  <text class="sans benefits" x="275" y="176" text-anchor="middle">SUPPORT • CALM • EASE</text>

  <text class="sans product-name" x="275" y="252" text-anchor="middle">SnuggleBites</text>
  <ellipse class="cbd-pill" cx="405" cy="268" rx="31" ry="14" fill="var(--brand-green)"/>
  <text class="sans cbd-tag" x="405" y="275" text-anchor="middle">CBD</text>
  <text class="treats-word" x="312" y="340" transform="rotate(-6 400 320)">Treats</text>

  <text class="flavour flavour-top" x="289" y="390">Simply</text>
  <text class="flavour flavour-main" x="313" y="434">Chicken</text>

  <path class="frame-curve" fill="var(--brand-green)"
        d="M250 560 C262 500 320 455 400 450 C420 449 438 452 448 458 C430 466 410 470 400 472 C320 482 262 520 250 575 Z"/>
  <path class="bottom-band" fill="var(--brand-green)"
        d="M0 668 H230 C255 668 268 650 276 625 C284 650 300 668 330 668 H550 V690 H330 C305 690 285 680 276 662 C267 680 250 690 225 690 H0 Z"/>

  <ellipse class="treats-photo" role="img" aria-label="Photo of bone-shaped chicken treats"
           cx="365" cy="570" rx="123" ry="90" fill="var(--treat)"/>

  <path class="dog-photo" role="img" aria-label="Photo of the white wrinkled brand ambassador dog"
        d="M0 530 C15 460 30 390 55 310 C90 285 150 285 200 300 C240 310 262 340 262 390 C262 430 270 460 278 490 C285 530 270 560 250 590 C240 620 235 645 235 668 H0 Z"
        fill="var(--dog-fur)"/>
  <path class="puppy-photo" role="img" aria-label="Photo of a puppy resting its paws on the edge"
        d="M372 640 C380 600 410 585 440 588 C475 590 495 610 505 625 C525 640 550 655 550 700 V705 H380 C370 690 368 660 372 640 Z"
        fill="var(--dog-shade)"/>

  <g class="thc-badge">
    <circle cx="488" cy="486" r="46" fill="none" stroke="var(--brand-green)" stroke-width="4" stroke-dasharray="0.1 8" stroke-linecap="round"/>
    <circle cx="488" cy="486" r="37" fill="var(--ink)" stroke="var(--brand-green)" stroke-width="1.5"/>
    <text class="sans badge-big" x="488" y="484" text-anchor="middle" font-size="26">NO</text>
    <text class="sans badge-big" x="488" y="503" text-anchor="middle" font-size="19">THC</text>
    <text class="sans badge-small" x="488" y="515" text-anchor="middle">0% THC</text>
  </g>

  <text class="sans claim" x="275" y="734" text-anchor="middle">“Recommended By Veterinarians”</text>
</svg>
</body>
</html>
```